Tidal Fern Business Cards

We need something new, fun and exciting for business cards. Our current ones are just plain and we need a design that pops. We want name, position held, phone, email on the front, and a 20% discount on the back. I have also uploaded our old business cards creative to see what we are not wanting, and how boring they were and we want something jazzed up from this, cool design and catches people attention.

```html
<!DOCTYPE html>
<html lang="en">
<head>
<meta charset="utf-8">
<title>Tidal Fern Business Cards</title>
<link href="https://fonts.googleapis.com/css2?family=Montserrat:wght@400;500;700;800&display=swap" rel="stylesheet">
<style>
  :root {
    --backdrop: #3a3b3f;
    --navy: #1b3f78;
    --coral: #f07470;
    --white: #ffffff;
    --ink: #3d3d45;
    --paper-shade: #f5f6f9;
  }
  * { margin: 0; padding: 0; box-sizing: border-box; }
  html, body {
    width: 1200px; height: 900px; overflow: hidden;
    background: var(--backdrop);
    font-family: "Montserrat", sans-serif;
  }
  .stage {
    position: relative; width: 1200px; height: 900px;
    display: flex; justify-content: center; align-items: center; gap: 100px;
  }
  .card {
    position: relative; width: 300px; height: 525px;
    background: var(--white); overflow: hidden;
    box-shadow: 0 14px 30px rgba(0,0,0,0.35);
  }

  /* wordmark */
  .wordmark {
    display: flex; align-items: center; justify-content: center; gap: 10px;
    color: var(--navy); font-weight: 700; white-space: nowrap;
  }
  .wordmark-dot { border-radius: 50%; background: var(--coral); flex: none; }

  /* front */
  .front .wordmark { position: absolute; top: 92px; left: 0; right: 0; font-size: 38px; }
  .front .wordmark-dot { width: 20px; height: 20px; }
  .name-band {
    position: absolute; top: 200px; left: 0; right: 0; height: 82px;
    background: var(--navy);
    display: flex; flex-direction: column; justify-content: center; align-items: center;
  }
  .name-band::before, .name-band::after {
    content: ""; position: absolute; left: 0; right: 0; height: 2px; background: var(--coral);
  }
  .name-band::before { top: -7px; }
  .name-band::after { bottom: -7px; }
  .holder-name { color: var(--coral); font-weight: 700; font-size: 21px; letter-spacing: 0.5px; }
  .holder-role { color: var(--white); font-weight: 500; font-size: 15px; margin-top: 4px; }
  .address {
    position: absolute; top: 335px; left: 0; right: 0;
    text-align: center; color: var(--ink); font-size: 15px; line-height: 1.45;
  }
  .contact-icons {
    position: absolute; top: 390px; left: 0; right: 0;
    display: flex; justify-content: center; gap: 6px;
  }
  .contact-icons svg { width: 22px; height: 22px; }
  .contacts {
    position: absolute; top: 432px; left: 0; right: 0;
    text-align: center; color: var(--ink); font-size: 15.5px; line-height: 1.45;
  }

  /* back */
  .back { background: var(--paper-shade); }
  .back-top {
    position: absolute; top: 0; left: 0; right: 0; height: 215px; background: var(--navy);
  }
  .discount-badge {
    position: absolute; top: 142px; left: 112px; width: 150px; height: 150px;
    border-radius: 50%; background: var(--coral); border: 7px solid var(--white);
    display: flex; flex-direction: column; align-items: center; justify-content: center;
    color: var(--white);
  }
  .discount-value { font-weight: 800; font-size: 46px; line-height: 1; }
  .discount-label { font-weight: 700; font-size: 15px; letter-spacing: 1.5px; margin-top: 4px; }
  .back .wordmark { position: absolute; top: 400px; left: 0; right: 0; font-size: 46px; }
  .back .wordmark-dot { width: 24px; height: 24px; }
</style>
</head>
<body>
<main class="stage">

  <section class="card front" aria-label="Business card front">
    <div class="wordmark"><span class="wordmark-dot"></span>Tidal Fern</div>

    <div class="name-band">
      <p class="holder-name">DANA MERCER</p>
      <p class="holder-role">Founder &amp; CEO</p>
    </div>

    <p class="address">2715 W. Harlow St<br>Denver, CO 80219</p>

    <div class="contact-icons">
      <svg viewBox="0 0 22 22" aria-label="Phone">
        <circle cx="11" cy="11" r="10" fill="none" stroke="var(--coral)" stroke-width="2"/>
        <path d="M7.5 6.5l2 0 1 2.5-1.3 1a6 6 0 0 0 2.8 2.8l1-1.3 2.5 1 0 2c-4.5 .5-8.5-3.5-8-8z" fill="var(--coral)"/>
      </svg>
      <svg viewBox="0 0 22 22" aria-label="Email">
        <circle cx="11" cy="11" r="10" fill="none" stroke="var(--coral)" stroke-width="2"/>
        <rect x="6" y="7.5" width="10" height="7" fill="none" stroke="var(--coral)" stroke-width="1.5"/>
        <path d="M6 7.5l5 4 5-4" fill="none" stroke="var(--coral)" stroke-width="1.5"/>
      </svg>
      <svg viewBox="0 0 22 22" aria-label="Website">
        <circle cx="11" cy="11" r="10" fill="none" stroke="var(--coral)" stroke-width="2"/>
        <circle cx="11" cy="11" r="5" fill="none" stroke="var(--coral)" stroke-width="1.4"/>
        <path d="M6 11h10M11 6c-2.5 3-2.5 7 0 10M11 6c2.5 3 2.5 7 0 10" fill="none" stroke="var(--coral)" stroke-width="1.2"/>
      </svg>
    </div>

    <p class="contacts">(302) 555-0147<br>info@tidalfern.com<br>www.tidalfern.com</p>
  </section>

  <section class="card back" aria-label="Business card back">
    <div class="back-top"></div>
    <div class="discount-badge">
      <span class="discount-value">20%</span>
      <span class="discount-label">DISCOUNT</span>
    </div>
    <div class="wordmark"><span class="wordmark-dot"></span>Tidal Fern</div>
  </section>

</main>
</body>
</html>
```